Business card design needed

We design, manufacture and install kitchen robes vanity etc.
We have a current card that i want to upload that you can base the design around and make suggestions for other design but we need the logo to be unchanged that i will up load along with our current card.

Industry/Entity Type

Business

Contact Information for Business Card

Marlowe Cabinet Studio
Daniel Ferricott
27 Brindlemere Avenue, Harwick S.A 5082
daniel@marlowecabinet.com.au
Lic. No. Bld 274958 Bld 291436

```html
<!DOCTYPE html>
<html lang="en">
<head>
<meta charset="utf-8">
<title>Marlowe Cabinet Studio Business Card</title>
<link href="https://fonts.googleapis.com/css2?family=Exo+2:wght@400;600&display=swap" rel="stylesheet">
<style>
  :root {
    --backdrop: #d3d3d3;
    --card-white: #ffffff;
    --band-dark: #1c1c1c;
    --band-mid: #2c2c2c;
    --accent-green: #8aa03a;
    --logo-grey: #b9b9b9;
    --text-dark: #2a2a2a;
  }
  html, body {
    margin: 0;
    width: 1200px;
    height: 861px;
    overflow: hidden;
    background: var(--backdrop);
    font-family: "Exo 2", sans-serif;
  }
  .stage {
    position: relative;
    width: 1200px;
    height: 861px;
  }
  .card {
    position: absolute;
    top: 288px;
    width: 500px;
    height: 286px;
    background: var(--card-white);
    box-shadow: 0 6px 18px rgba(0,0,0,0.18);
    overflow: hidden;
  }
  .card--front { left: 60px; }
  .card--back { left: 640px; }
  .card__band {
    position: absolute;
    left: 0; top: 0;
    width: 100%;
    height: 132px;
    background: linear-gradient(135deg, var(--band-mid), var(--band-dark));
    border-bottom: 6px solid var(--accent-green);
  }
  .brand {
    position: absolute;
    display: flex;
    align-items: center;
    gap: 10px;
    font-weight: 600;
    font-size: 22px;
    letter-spacing: 0.5px;
    color: var(--logo-grey);
    text-transform: uppercase;
    white-space: nowrap;
  }
  .brand__mark {
    width: 14px;
    height: 14px;
    background: var(--accent-green);
  }
  .card--front .brand { right: 28px; bottom: 18px; }
  .card--back .brand { left: 50%; transform: translateX(-50%); bottom: 22px; }

  .person {
    position: absolute;
    right: 28px;
    top: 150px;
    margin: 0;
    font-size: 22px;
    font-weight: 600;
    color: var(--accent-green);
  }
  .contacts {
    position: absolute;
    left: 26px;
    top: 152px;
    margin: 0;
    padding: 0;
    list-style: none;
    font-size: 14px;
    line-height: 22px;
    color: var(--text-dark);
  }
  .contacts__key {
    display: inline-block;
    width: 18px;
    font-weight: 600;
    color: var(--accent-green);
  }

  .services {
    position: absolute;
    left: 0; right: 0;
    top: 150px;
    text-align: center;
    color: var(--text-dark);
  }
  .services__title {
    margin: 0 0 6px;
    font-size: 21px;
    font-weight: 400;
    letter-spacing: 0.5px;
    color: var(--accent-green);
  }
  .services__list {
    margin: 0;
    font-size: 17px;
    line-height: 23px;
  }
  .licence {
    margin: 10px 0 0;
    font-size: 13px;
  }
  .licence__label {
    color: var(--accent-green);
    font-weight: 600;
  }
</style>
</head>
<body>
<main class="stage">

  <section class="card card--front" aria-label="Business card front">
    <div class="card__band" role="img" aria-label="Dark faceted triangle texture band">
      <div class="brand"><span class="brand__mark"></span>Marlowe Cabinet Studio</div>
    </div>
    <p class="person">Daniel Ferricott</p>
    <ul class="contacts">
      <li><span class="contacts__key">A</span>27 Brindlemere Avenue, Harwick S.A 5082</li>
      <li><span class="contacts__key">M</span>0491 570 156</li>
      <li><span class="contacts__key">P</span>(08) 7010 4832</li>
      <li><span class="contacts__key">F</span>(08) 7010 4839</li>
      <li><span class="contacts__key">E</span>daniel@marlowecabinet.com.au</li>
    </ul>
  </section>

  <section class="card card--back" aria-label="Business card back">
    <div class="card__band" role="img" aria-label="Dark faceted triangle texture band">
      <div class="brand"><span class="brand__mark"></span>Marlowe Cabinet Studio</div>
    </div>
    <div class="services">
      <h2 class="services__title">CUSTOM MADE</h2>
      <p class="services__list">Kitchen • Vanities • Laundry<br>Robes • Entertainment Units • Flat Packs</p>
      <p class="licence"><span class="licence__label">License Number</span> Bld. 274958, Bld. 291436</p>
    </div>
  </section>

</main>
</body>
</html>
```